Infographic for B2B Service solution offering (sales funnel)

Attached is an example of something we need assistance with making into a more professional infographic. These infographics are for our B2B marketing services, aimed at IT Consulting firms.

We have done some basic graphics (attached) and this will provide you guidance (video link on google sheet):
https://files.plonkaret.com/doc/7kQm2Rvx9TbLw4PzHn3YcJa8EuVd6SgFi1MoXp5Ct/view?mode=share

Here are some examples you can model for the new infographic:
https://store.vendrilo.net/box/folders/84TpKwa3Mz9Rj2Lbn6Yq-Hfx5CeGsv?ref=box_link

Target Market(s)

B2B IT Consulting Firms

Industry/Entity Type

Information Technology, Consulting

Colors

Designer to choose colors to be used in the design.

Requirements
Must have
• professional, high level consulting firms are target market
Should not have
• cartoonish

```html
<!DOCTYPE html>
<html lang="en">
<head>
<meta charset="utf-8">
<title>How Relationships Are Built – Trust Building Offers</title>
<link rel="stylesheet" href="https://fonts.googleapis.com/css2?family=Archivo+Black&family=Fira+Sans:ital,wght@0,700;1,600&family=Roboto:wght@500;700&display=swap">
<style>
  :root {
    --bg-left: #c4e2e9;
    --bg-right: #effcfb;
    --title-red: #9b0a1a;
    --navy: #0b2a78;
    --trust-low: #f01010;
    --trust-high: #1fa31f;
    --white: #ffffff;
  }
  html, body {
    margin: 0;
    padding: 0;
    width: 1200px;
    height: 1200px;
    overflow: hidden;
  }
  .infographic {
    display: block;
    width: 1200px;
    height: 1200px;
  }
  .title {
    font-family: "Fira Sans", sans-serif;
    font-style: italic;
    font-weight: 600;
    font-size: 66px;
    fill: var(--title-red);
    text-anchor: middle;
  }
  .heading {
    font-family: "Archivo Black", sans-serif;
    font-size: 88px;
    fill: var(--navy);
  }
  .cold-leads {
    font-family: "Fira Sans", sans-serif;
    font-weight: 700;
    font-size: 36px;
    fill: var(--navy);
    text-anchor: middle;
  }
  .stage-label {
    font-family: "Fira Sans", sans-serif;
    font-weight: 700;
    font-size: 36px;
    fill: var(--white);
    text-anchor: middle;
  }
  .offer-tab-label {
    font-family: "Roboto", sans-serif;
    font-weight: 700;
    font-size: 36px;
    fill: var(--white);
    text-anchor: middle;
  }
  .offer-terms {
    font-family: "Roboto", sans-serif;
    font-weight: 500;
    font-size: 28px;
    fill: var(--white);
  }
  .trust-label {
    font-family: "Fira Sans", sans-serif;
    font-weight: 700;
    font-size: 36px;
  }
  .trust-low { fill: var(--trust-low); }
  .trust-high { fill: var(--trust-high); }
</style>
</head>
<body>
<svg class="infographic" viewBox="0 0 1932 1932" xmlns="http://www.w3.org/2000/svg">
  <defs>
    <linearGradient id="bg" x1="0" y1="0" x2="1" y2="0">
      <stop offset="0" stop-color="#c4e2e9"/>
      <stop offset="1" stop-color="#effcfb"/>
    </linearGradient>
    <linearGradient id="trust-line" x1="0" y1="0" x2="0" y2="1">
      <stop offset="0" stop-color="#f01010"/>
      <stop offset="0.3" stop-color="#f5a000"/>
      <stop offset="0.55" stop-color="#f0f000"/>
      <stop offset="1" stop-color="#1fa31f"/>
    </linearGradient>

    <linearGradient id="phone-body" x1="0" y1="0" x2="1" y2="0">
      <stop offset="0" stop-color="#0a4fc0"/>
      <stop offset="0.45" stop-color="#2c90ef"/>
      <stop offset="0.75" stop-color="#5cc6ff"/>
      <stop offset="1" stop-color="#2e9af7"/>
    </linearGradient>
    <linearGradient id="coffee-body" x1="0" y1="0" x2="1" y2="0">
      <stop offset="0" stop-color="#03256b"/>
      <stop offset="0.4" stop-color="#0a4fb0"/>
      <stop offset="0.8" stop-color="#3593e0"/>
      <stop offset="1" stop-color="#0a52b8"/>
    </linearGradient>
    <linearGradient id="dinner-body" x1="0" y1="0" x2="1" y2="0">
      <stop offset="0" stop-color="#6e0010"/>
      <stop offset="0.4" stop-color="#b3001c"/>
      <stop offset="0.8" stop-color="#d41e4c"/>
      <stop offset="1" stop-color="#b80020"/>
    </linearGradient>
    <linearGradient id="weekend-body" x1="0" y1="0" x2="1" y2="0">
      <stop offset="0" stop-color="#0f1f38"/>
      <stop offset="0.5" stop-color="#28466a"/>
      <stop offset="0.8" stop-color="#46739a"/>
      <stop offset="1" stop-color="#213b57"/>
    </linearGradient>
    <linearGradient id="parents-body" x1="0" y1="0" x2="1" y2="0">
      <stop offset="0" stop-color="#2c3436"/>
      <stop offset="0.55" stop-color="#566466"/>
      <stop offset="0.85" stop-color="#7c9290"/>
      <stop offset="1" stop-color="#4e5c5f"/>
    </linearGradient>
    <linearGradient id="movein-body" x1="0" y1="0" x2="1" y2="0">
      <stop offset="0" stop-color="#15191c"/>
      <stop offset="0.6" stop-color="#343a40"/>
      <stop offset="1" stop-color="#4a5158"/>
    </linearGradient>
    <linearGradient id="wife-body" x1="0" y1="0" x2="1" y2="0">
      <stop offset="0" stop-color="#8a0014"/>
      <stop offset="0.5" stop-color="#d0001e"/>
      <stop offset="1" stop-color="#e0244a"/>
    </linearGradient>

    <linearGradient id="ribbon-1" x1="0" y1="0" x2="1" y2="0">
      <stop offset="0.6" stop-color="#2e9af7"/><stop offset="1" stop-color="#1d3a5c"/>
    </linearGradient>
    <linearGradient id="ribbon-2" x1="0" y1="0" x2="1" y2="0">
      <stop offset="0.65" stop-color="#0a52b8"/><stop offset="1" stop-color="#1b2a44"/>
    </linearGradient>
    <linearGradient id="ribbon-3" x1="0" y1="0" x2="1" y2="0">
      <stop offset="0.65" stop-color="#c0001a"/><stop offset="1" stop-color="#3a1a22"/>
    </linearGradient>
    <linearGradient id="ribbon-4" x1="0" y1="0" x2="1" y2="0">
      <stop offset="0.6" stop-color="#213b57"/><stop offset="1" stop-color="#1a2638"/>
    </linearGradient>
    <linearGradient id="ribbon-5" x1="0" y1="0" x2="1" y2="0">
      <stop offset="0.6" stop-color="#4e5c5f"/><stop offset="1" stop-color="#252d2f"/>
    </linearGradient>
    <linearGradient id="ribbon-6" x1="0" y1="0" x2="1" y2="0">
      <stop offset="0.6" stop-color="#2e3338"/><stop offset="1" stop-color="#1a1d20"/>
    </linearGradient>
    <linearGradient id="ribbon-7" x1="0" y1="0" x2="1" y2="0">
      <stop offset="0.6" stop-color="#c8001a"/><stop offset="1" stop-color="#3a1a22"/>
    </linearGradient>
  </defs>

  <rect width="1932" height="1932" fill="url(#bg)"/>

  <!-- Header -->
  <g class="header">
    <text class="title" x="965" y="215">Creating B2B Relationships</text>
    <text class="title" x="965" y="298">The Rise Tech “Trust Building Offers” Method</text>
    <line x1="288" y1="350" x2="1643" y2="350" stroke="#9b0a1a" stroke-width="4"/>
    <text class="heading" x="288" y="452" textLength="1355" lengthAdjust="spacingAndGlyphs">HOW RELATIONSHIPS ARE BUILT</text>
  </g>

  <!-- Cold leads marker -->
  <g class="cold-leads-marker">
    <text class="cold-leads" x="1094" y="660">COLD LEADS</text>
    <line x1="1094" y1="692" x2="1094" y2="780" stroke="#0b2a78" stroke-width="2" stroke-dasharray="3 4"/>
    <path d="M1086,694 L1094,682 L1102,694 Z" fill="#0b2a78"/>
    <path d="M1086,776 L1094,788 L1102,776 Z" fill="#0b2a78"/>
  </g>

  <!-- Offer ribbons (behind funnel) -->
  <g class="offer-ribbons">
    <path d="M265,805 H680 L735,975 H368 C358,900 335,828 265,812 Z" fill="url(#ribbon-1)"/>
    <path d="M360,1032 H745 L800,1185 H452 C442,1115 420,1050 360,1040 Z" fill="url(#ribbon-2)"/>
    <path d="M432,1230 H815 L865,1377 H518 C508,1310 490,1248 432,1238 Z" fill="url(#ribbon-3)"/>
    <path d="M492,1400 H875 L918,1513 H568 C558,1460 540,1412 492,1406 Z" fill="url(#ribbon-4)"/>
    <path d="M535,1532 H920 L953,1621 H608 C598,1575 582,1540 535,1536 Z" fill="url(#ribbon-5)"/>
    <path d="M570,1647 H960 L992,1721 H643 C633,1680 618,1652 570,1650 Z" fill="url(#ribbon-6)"/>
    <path d="M617,1740 H998 L1028,1804 H668 C660,1768 648,1745 617,1743 Z" fill="url(#ribbon-7)"/>
  </g>

  <!-- Offer tabs -->
  <g class="offer-tabs">
    <rect x="97" y="840" width="300" height="92" rx="18" fill="#2e9af7"/>
    <rect x="177" y="1065" width="280" height="87" rx="16" fill="#0a52b8"/>
    <rect x="247" y="1264" width="280" height="80" rx="16" fill="#c0001a"/>
    <rect x="308" y="1420" width="270" height="74" rx="14" fill="#213b57"/>
    <rect x="349" y="1543" width="270" height="68" rx="14" fill="#4e5c5f"/>
    <rect x="392" y="1653" width="260" height="62" rx="13" fill="#2e3338"/>
    <rect x="429" y="1745" width="250" height="54" rx="12" fill="#c8001a"/>

    <text class="offer-tab-label" x="218" y="898">Offer 1</text>
    <text class="offer-tab-label" x="302" y="1121">Offer 2</text>
    <text class="offer-tab-label" x="371" y="1317">Offer 3</text>
    <text class="offer-tab-label" x="425" y="1470">Offer 4</text>
    <text class="offer-tab-label" x="470" y="1590">Offer 5</text>
    <text class="offer-tab-label" x="509" y="1697">Offer 6</text>
    <text class="offer-tab-label" x="538" y="1785">Offer 7</text>
  </g>

  <g class="offer-terms-group">
    <text class="offer-terms" x="394" y="882">LOW RISK,</text>
    <text class="offer-terms" x="394" y="909">LOW INVESTMENT</text>
    <text class="offer-terms" x="476" y="1103">LOW RISK,</text>
    <text class="offer-terms" x="476" y="1131">MEDIUM INVESTMENT</text>
    <text class="offer-terms" x="542" y="1300">MEDIUM RISK,</text>
    <text class="offer-terms" x="542" y="1328">MEDIUM INVESTMENT</text>
    <text class="offer-terms" x="600" y="1453">HIGH RISK,</text>
    <text class="offer-terms" x="600" y="1480">MEDIUM INVESTMENT</text>
    <text class="offer-terms" x="646" y="1573">MEDIUM RISK,</text>
    <text class="offer-terms" x="646" y="1600">HIGH INVESTMENT</text>
    <text class="offer-terms" x="682" y="1680">HIGH RISK,</text>
    <text class="offer-terms" x="682" y="1707">HIGH INVESTMENT</text>
    <text class="offer-terms" x="716" y="1768">HIGH RISK,</text>
    <text class="offer-terms" x="716" y="1795">HIGH INVESTMENT</text>
  </g>

  <!-- Funnel stages, bottom first so upper stages overlap -->
  <g class="funnel">
    <g class="stage stage-wife">
      <ellipse cx="1086" cy="1744" rx="91" ry="15" fill="#8a0014"/>
      <path d="M995,1744 L1022,1800 Q1090,1814 1155,1800 L1177,1744 Q1086,1762 995,1744 Z" fill="url(#wife-body)"/>
      <text class="stage-label" x="1086" y="1796">WIFE</text>
    </g>
    <g class="stage stage-move-in">
      <ellipse cx="1083" cy="1648" rx="125" ry="22" fill="#23282c"/>
      <path d="M958,1648 L988,1725 Q1085,1748 1185,1722 L1208,1648 Q1083,1676 958,1648 Z" fill="url(#movein-body)"/>
      <text class="stage-label" x="1084" y="1712" transform="rotate(-2 1084 1712)">MOVE IN</text>
    </g>
    <g class="stage stage-meet-parents">
      <ellipse cx="1083" cy="1540" rx="165" ry="25" fill="#3b4747"/>
      <path d="M918,1540 L950,1620 Q1085,1646 1218,1614 L1248,1540 Q1083,1572 918,1540 Z" fill="url(#parents-body)"/>
      <text class="stage-label" x="1083" y="1606" transform="rotate(-2 1083 1606)">MEET PARENTS</text>
    </g>
    <g class="stage stage-weekend-travel">
      <ellipse cx="1083" cy="1404" rx="211" ry="30" fill="#172a44"/>
      <path d="M872,1404 L913,1505 Q1085,1540 1253,1502 L1294,1404 Q1083,1442 872,1404 Z" fill="url(#weekend-body)"/>
      <text class="stage-label" x="1085" y="1498" transform="rotate(-2 1085 1498)">WEEKEND TRAVEL</text>
    </g>
    <g class="stage stage-dinner">
      <ellipse cx="1086" cy="1226" rx="276" ry="42" fill="#8a0018"/>
      <path d="M810,1226 L858,1372 Q1085,1415 1310,1368 L1362,1226 Q1086,1272 810,1226 Z" fill="url(#dinner-body)"/>
      <text class="stage-label" x="1083" y="1355">DINNER</text>
    </g>
    <g class="stage stage-coffee">
      <ellipse cx="1086" cy="1030" rx="348" ry="58" fill="#0a4a85"/>
      <path d="M738,1030 L796,1196 Q1085,1250 1376,1190 L1434,1030 Q1086,1092 738,1030 Z" fill="url(#coffee-body)"/>
      <text class="stage-label" x="1086" y="1180">COFFEE</text>
    </g>
    <g class="stage stage-phone">
      <path d="M670,800 L732,985 Q1090,1075 1455,970 L1516,805 Q1093,880 670,800 Z" fill="url(#phone-body)"/>
      <ellipse cx="1093" cy="797" rx="423" ry="75" fill="#2f9bf5"/>
      <ellipse cx="1083" cy="800" rx="400" ry="56" fill="#2b86dc"/>
      <text class="stage-label" x="1084" y="955">PHONE</text>
    </g>
  </g>

  <!-- Trust scale -->
  <g class="trust-scale">
    <line x1="1573" y1="745" x2="1573" y2="1782" stroke="url(#trust-line)" stroke-width="6" stroke-dasharray="16 9"/>
    <path d="M1533,1740 L1573,1792 L1612,1740" fill="none" stroke="#1fa31f" stroke-width="4"/>
    <text class="trust-label trust-low" x="1625" y="770">LOW TRUST</text>
    <text class="trust-label trust-high" x="1625" y="1775">HIGH TRUST</text>
  </g>
</svg>
</body>
</html>
```